" A brisas do Lumaré é uma empresa produtora de polpas de frutas congeladas, sumos naturais, e gelados artesanais. comercialisamos os produtos para lojas, e restaurants. funcianamento: a materia prima (fruta) chega a fabrica, e é processeda segungo um protocolo definido pelas normas de saude e higiene. posterioremente é embalado e armazenado. os pedidos dos clientes chegam por telefone ou whatsaap e nós procedemos de acordo. fazemos entregas ou o cliente vem até a fabrica. em junho sera aberta a loja/restaurante/gelataria fisica. todos os products são processados por nós. usamos produtos de qualidade, sem corantes e sem conservantes artificiais. promovemos alternativas ao convencional. "

```html
<!DOCTYPE html>
<html lang="pt">
<head>
<meta charset="UTF-8">
<title>Brisas do Lumaré — Faixa Sabor Saudável</title>
<link href="https://fonts.googleapis.com/css2?family=Montserrat:wght@600;700;800&family=Kaushan+Script&display=swap" rel="stylesheet">
<style>
  :root {
    --page-bg: #f1e6cf;
    --banner-red: #8e1414;
    --banner-red-dark: #5e0a0a;
    --banner-red-light: #b02020;
    --gold: #f2a51e;
    --white: #ffffff;
    --cream: #f7e9d2;
    --fruit-orange: #f39a1a;
    --fruit-yellow: #f7d55a;
    --fruit-brown: #8a5a2b;
  }
  html, body {
    margin: 0;
    padding: 0;
    width: 1200px;
    height: 1200px;
    overflow: hidden;
    background: var(--page-bg);
  }
  .canvas {
    position: relative;
    width: 1200px;
    height: 1200px;
  }
  .banner {
    position: absolute;
    left: 50px;
    top: 374px;
    width: 1100px;
    height: 452px;
    background:
      radial-gradient(ellipse at 55% 45%, var(--banner-red-light) 0%, var(--banner-red) 45%, var(--banner-red-dark) 100%);
    overflow: hidden;
    font-family: "Montserrat", sans-serif;
    color: var(--white);
  }
  .brand {
    position: absolute;
    left: 40px;
    top: 70px;
    width: 300px;
    display: flex;
    flex-direction: column;
    align-items: center;
  }
  .brand-dot {
    width: 30px;
    height: 30px;
    border-radius: 50%;
    background: var(--gold);
    margin-bottom: 18px;
  }
  .brand-name {
    font-weight: 700;
    font-size: 46px;
    line-height: 1.05;
    color: var(--gold);
    text-align: center;
    margin: 0;
  }
  .brand-tagline {
    margin-top: 10px;
    font-weight: 600;
    font-size: 15px;
    letter-spacing: 4px;
    color: var(--gold);
  }
  .product-list {
    position: absolute;
    left: 22px;
    top: 302px;
    margin: 0;
    padding: 0;
    list-style: none;
    font-weight: 800;
    font-size: 15.5px;
    line-height: 1.75;
    text-transform: uppercase;
  }
  .product-list li:nth-child(2) { padding-left: 22px; }
  .product-list li:nth-child(3) { padding-left: 44px; }
  .product-visual {
    position: absolute;
    left: 300px;
    top: 0;
    width: 560px;
    height: 400px;
  }
  .headline {
    position: absolute;
    right: 40px;
    top: 70px;
    width: 300px;
    margin: 0;
    font-family: "Kaushan Script", cursive;
    font-weight: 400;
    font-size: 80px;
    line-height: 1.05;
    text-align: center;
    color: var(--white);
  }
  .contact-line {
    position: absolute;
    right: 24px;
    bottom: 12px;
    margin: 0;
    font-weight: 600;
    font-size: 13.5px;
    color: var(--cream);
    letter-spacing: 0.3px;
  }
</style>
</head>
<body>
<main class="canvas">
  <section class="banner">
    <div class="brand">
      <span class="brand-dot"></span>
      <h1 class="brand-name">Brisas do<br>Lumaré</h1>
      <span class="brand-tagline">POLPAS DE FRUTA</span>
    </div>

    <ul class="product-list">
      <li>- Polpas de fruta - Sumos naturais</li>
      <li>- Batidos detox - Mousses</li>
      <li>- E muito mais</li>
    </ul>

    <svg class="product-visual" viewBox="0 0 560 400" role="img" aria-label="Fotografia de dois copos de sumo de fruta, vermelho e amarelo, com salpicos, rodeados de tamarindo, frutos secos e laranjinhas">
      <defs>
        <radialGradient id="visual-red" cx="0.4" cy="0.45" r="0.5">
          <stop offset="0" stop-color="#e8402a" stop-opacity="0.9"/>
          <stop offset="1" stop-color="#e8402a" stop-opacity="0"/>
        </radialGradient>
        <radialGradient id="visual-yellow" cx="0.6" cy="0.45" r="0.45">
          <stop offset="0" stop-color="#f7d55a" stop-opacity="0.95"/>
          <stop offset="1" stop-color="#f7d55a" stop-opacity="0"/>
        </radialGradient>
        <radialGradient id="visual-orange" cx="0.72" cy="0.75" r="0.3">
          <stop offset="0" stop-color="#f39a1a" stop-opacity="0.9"/>
          <stop offset="1" stop-color="#f39a1a" stop-opacity="0"/>
        </radialGradient>
        <radialGradient id="visual-brown" cx="0.25" cy="0.7" r="0.35">
          <stop offset="0" stop-color="#8a5a2b" stop-opacity="0.9"/>
          <stop offset="1" stop-color="#8a5a2b" stop-opacity="0"/>
        </radialGradient>
      </defs>
      <rect width="560" height="400" fill="url(#visual-brown)"/>
      <rect width="560" height="400" fill="url(#visual-red)"/>
      <rect width="560" height="400" fill="url(#visual-orange)"/>
      <rect width="560" height="400" fill="url(#visual-yellow)"/>
    </svg>

    <h2 class="headline">Sabor<br>Saudável</h2>

    <p class="contact-line">Rua das Acácias, 412 - Vila Nova - Luanda | (11) 4021-7730 / 4021-7731 | www.brisasdolumare.com</p>
  </section>
</main>
</body>
</html>
```